New Business Card for Innovative Tool Company

We need a new design of business card for our florida based tool manufacturing company. I will attach 2 files that we use for our logo, use whichever you feel works best for the card. Main colours are as per logo, and we can use different shades of black/white/grey for the background.

Contact Information for Business Card

Name/Jobtitle/cell
Brackwell Tools
Suite 214c
3190 Harlowmere Pkw
Marrowgate, FL30417
USA
name@brackwellco.example
www.brackwellco.example

Font styles to use
Sans Serif

Colors

Designer to choose colors to be used in the design.

Requirements
Must have
• Icons for Chatterly, Quiplet, Snapvista, Findora & Viewtube

```html
<!DOCTYPE html>
<html lang="en">
<head>
<meta charset="utf-8">
<title>Brackwell Tools – Business Card</title>
<link rel="stylesheet" href="https://fonts.googleapis.com/css2?family=Roboto:wght@400;700;900&display=swap">
<style>
  :root {
    --backdrop: #3c3c3e;
    --card-grey: #55565a;
    --card-shadow: #333335;
    --brand-yellow: #f5ea2e;
    --text-white: #f2f2f2;
  }
  * { box-sizing: border-box; margin: 0; padding: 0; }
  html, body {
    width: 1200px; height: 1000px; overflow: hidden;
    background: var(--backdrop);
    font-family: "Roboto", Arial, sans-serif;
  }
  .card {
    position: absolute; left: 250px;
    width: 700px; height: 400px;
    background: var(--card-grey);
    border-radius: 22px; overflow: hidden;
    box-shadow: 0 10px 30px rgba(0,0,0,.35);
  }
  .card-back { top: 60px; }
  .card-front { top: 540px; }

  /* back side */
  .back-mark {
    position: absolute; left: 50%; top: 50%;
    transform: translate(-50%, -50%);
    width: 300px; height: 240px;
    border: 2px solid var(--brand-yellow); border-radius: 50%;
    display: flex; align-items: center; justify-content: center;
  }
  .back-mark .brand-name {
    font-weight: 900; font-size: 30px; color: var(--brand-yellow);
    text-transform: uppercase; letter-spacing: 1px; text-align: center; line-height: 1.1;
  }

  /* front side */
  .holder { position: absolute; left: 40px; top: 62px; color: var(--text-white); }
  .holder-name {
    font-weight: 700; font-size: 22px; color: var(--brand-yellow);
    text-transform: uppercase; letter-spacing: .5px;
  }
  .holder-title { font-size: 15px; margin-left: 14px; }
  .address { margin-top: 14px; font-size: 16px; line-height: 1.4; color: var(--text-white); }
  .social { display: flex; gap: 12px; margin-top: 16px; list-style: none; }
  .social li {
    width: 24px; height: 24px; border-radius: 50%;
    background: var(--brand-yellow);
  }
  .divider {
    position: absolute; left: 40px; right: 70px; top: 250px;
    height: 1px; background: var(--brand-yellow);
  }
  .front-brand {
    position: absolute; right: 50px; top: 34px;
    display: flex; flex-direction: column; align-items: center; gap: 10px;
  }
  .front-brand .brand-circle {
    width: 86px; height: 70px; border-radius: 50%;
    border: 1.5px solid var(--brand-yellow);
  }
  .front-brand .brand-name {
    font-weight: 900; font-size: 30px; color: var(--brand-yellow);
    text-transform: uppercase; letter-spacing: 1px;
  }
  .contacts {
    position: absolute; right: 70px; top: 268px;
    list-style: none; color: var(--text-white); font-size: 17px; line-height: 1.55;
  }
  .contacts li { display: flex; align-items: center; gap: 8px; }
  .contacts svg { width: 14px; height: 14px; flex: none; }
  .edge-band { position: absolute; left: 0; bottom: 0; width: 700px; height: 90px; }
</style>
</head>
<body>

<section class="card card-back" aria-label="Card back">
  <div class="back-mark">
    <span class="brand-name">Brackwell<br>Tools</span>
  </div>
</section>

<section class="card card-front" aria-label="Card front">
  <div class="holder">
    <p><span class="holder-name">Daniel Roe</span><span class="holder-title">Managing Director</span></p>
    <p class="address">Suite 214c 3190 Harlowmere<br>Pkw Marrowgate, FL30417 USA</p>
    <ul class="social" aria-label="Social profiles">
      <li aria-label="Chatterly"></li>
      <li aria-label="Quiplet"></li>
      <li aria-label="Viewtube"></li>
      <li aria-label="Findora"></li>
      <li aria-label="Snapvista"></li>
    </ul>
  </div>

  <div class="front-brand">
    <span class="brand-circle"></span>
    <span class="brand-name">Brackwell Tools</span>
  </div>

  <div class="divider"></div>

  <ul class="contacts">
    <li>
      <svg viewBox="0 0 14 14"><rect x="1" y="3" width="12" height="8" fill="#f5ea2e"/><path d="M1 3l6 4.5L13 3" fill="none" stroke="#55565a" stroke-width="1.2"/></svg>
      name@brackwellco.example
    </li>
    <li>
      <svg viewBox="0 0 14 14"><circle cx="7" cy="7" r="6" fill="#f5ea2e"/><path d="M1 7h12M7 1c-3 3.5-3 8.5 0 12M7 1c3 3.5 3 8.5 0 12" fill="none" stroke="#55565a" stroke-width=".9"/></svg>
      www.brackwellco.example
    </li>
  </ul>

  <svg class="edge-band" viewBox="0 0 700 90" preserveAspectRatio="none" aria-hidden="true">
    <path d="M0 50 H380 Q395 50 402 62 L410 74 H0 Z" fill="var(--card-shadow)"/>
    <path d="M0 72 H400 Q412 72 420 60 Q428 46 445 46 H700 V90 H0 Z" fill="var(--brand-yellow)"/>
  </svg>
</section>

</body>
</html>
```